Flyer Template Design

I have attached 4 files. I would like a design template that could be used across these documents so that they have a common look and feel. The content of the documents is tested and should not be changed significantly. The images can be changed. I have also attache our logo for color compatibility.
Updates

Need extra days to review

Target Market(s)

Wealthy Christian donors

Font styles to use
Serif
Sans Serif

```html
<!DOCTYPE html>
<html lang="en">
<head>
<meta charset="utf-8">
<title>Hastening His Coming – Flyer</title>
<link rel="stylesheet" href="https://fonts.googleapis.com/css2?family=Lato:ital,wght@0,400;0,700;0,900;1,400&family=Montserrat:wght@800;900&display=swap">
<style>
  :root {
    --backdrop: #e6e6e6;
    --paper: #ffffff;
    --ink: #2a2a2a;
    --ink-soft: #3d3d3d;
    --brand-green: #6fbe44;
    --brand-blue: #5bc4ec;
    --brand-dark: #2f6b3a;
    --photo-light: #f4f6f2;
    --photo-mid: #b9c6b4;
    --photo-deep: #4f5f4c;
  }
  * { box-sizing: border-box; margin: 0; padding: 0; }
  html, body {
    width: 1200px; height: 900px; overflow: hidden;
    background: var(--backdrop);
  }
  .flyer {
    position: absolute; left: 296px; top: 20px;
    width: 608px; height: 860px;
    background: var(--paper);
    overflow: hidden;
    box-shadow: 0 6px 24px rgba(0,0,0,0.12);
    font-family: "Lato", sans-serif;
    color: var(--ink-soft);
  }
  .flyer__photo {
    position: absolute; left: 0; right: 0; top: 400px; bottom: 0;
    background:
      radial-gradient(ellipse at 55% 55%, rgba(255,255,255,0.55), rgba(255,255,255,0) 45%),
      linear-gradient(180deg, var(--paper) 0%, var(--photo-light) 18%, var(--photo-mid) 55%, var(--photo-deep) 100%);
  }
  .flyer__content {
    position: relative; z-index: 1;
    padding: 34px 50px 0;
  }
  .brand {
    display: flex; align-items: center; justify-content: center; gap: 10px;
    margin-bottom: 14px;
  }
  .brand__mark {
    width: 30px; height: 30px; background: var(--brand-green);
  }
  .brand__name {
    font-family: "Lato", sans-serif; font-weight: 400;
    font-size: 14px; line-height: 1.1; letter-spacing: 0.06em;
    text-transform: uppercase; color: var(--ink);
  }
  .flyer__title {
    font-family: "Montserrat", sans-serif; font-weight: 900;
    font-size: 28px; text-align: center; color: var(--ink);
    letter-spacing: 0.01em; margin-bottom: 8px;
  }
  .section-title {
    font-family: "Montserrat", sans-serif; font-weight: 800;
    font-size: 15px; text-align: center; color: var(--ink);
    margin: 14px 0 6px;
  }
  .lead-title {
    font-weight: 900; font-size: 12.5px; text-align: center; color: var(--ink);
    line-height: 1.3; margin: 14px 0 5px;
  }
  p {
    font-size: 10.5px; line-height: 1.45;
  }
  p + p { margin-top: 10px; }
  em { font-style: italic; }
  .flyer__wave {
    position: absolute; left: 0; bottom: 0; width: 608px; height: 200px; z-index: 2;
  }
  .flyer__cta {
    position: absolute; left: 0; right: 0; bottom: 52px; z-index: 3;
    text-align: center; color: var(--paper);
    font-weight: 900; font-size: 14.5px; line-height: 1.35;
  }
</style>
</head>
<body>
  <article class="flyer">
    <div class="flyer__photo" role="img" aria-label="Photo of an open hand reaching up toward sunlight shining through blurred green trees"></div>

    <div class="flyer__content">
      <header class="brand">
        <span class="brand__mark"></span>
        <span class="brand__name">The Harvest<br>Completion Trust</span>
      </header>

      <h1 class="flyer__title">HASTENING HIS COMING</h1>
      <p>In his second letter, the Apostle Peter asks, what kind of people should believers be? He answers, “We ought to live holy and godly lives, looking for and <em>hastening the coming of the day of God</em>.” But how can we do that? How is it possible to hasten the coming of that day?</p>

      <h2 class="section-title">“AND THEN THE END WILL COME”</h2>
      <p>When Jesus’ disciples asked Him, Tell us, what will be the sign of your coming and of the end of the age? He replied, This gospel of the kingdom will be preached in the whole world as a testimony to all nations, and then the end will come.”</p>

      <h3 class="lead-title">When will Jesus return?<br>He said, only after gospel has been preached to “all nations.”</h3>
      <p>In the Bible, the word “nations” refers to people groups: groups of people with common ethnicity, culture, and language. Amazingly, there are about 12,000 of these “nations” around the world—and Jesus commanded His church to preach the gospel to all of them! Today, there are still 500 people groups without a single believer. No one has ever gone to these remaining “unengaged” groups with the gospel. They do not know the name of Jesus.</p>
      <p>After 2000 years, isn’t it time that they all heard?</p>

      <h2 class="section-title">FINISHING THE TASK</h2>
      <p>So how can we “hasten the coming of the day of God?” By completing the work Jesus gave us to do! Jesus said He would not return until the gospel is preached to every nation, so that’s what we need to do: take the gospel to all the groups that have never once heard it. Fortunately, we now know who these last groups are and where they are located, by God’s grace it is possible that we can engage all of them with the gospel within the next 3 years.</p>

      <h3 class="lead-title">You can make that happen.</h3>
      <p>Partner with the Harvest Completion Trust and finance the missionaries who are taking the gospel for the first time to those last remaining people groups. Your investment will “hasten the coming of the day of God” by accelerating the effort to make “disciples in every nation.” In 2018, our partners helped take the gospel to 231 people groups in 35 countries.</p>
    </div>

    <svg class="flyer__wave" viewBox="0 0 608 200" aria-hidden="true">
      <path d="M0 150 C 140 90, 330 40, 608 40 L 608 58 C 340 60, 150 110, 0 170 Z" fill="var(--brand-blue)"/>
      <path d="M0 132 C 170 140, 380 40, 608 60 L 608 200 L 0 200 Z" fill="var(--brand-green)"/>
      <path d="M0 172 C 180 150, 400 190, 608 168 L 608 176 C 400 200, 180 162, 0 184 Z" fill="var(--brand-blue)"/>
      <path d="M0 184 C 180 162, 400 200, 608 176 L 608 200 L 0 200 Z" fill="var(--paper)"/>
    </svg>
    <p class="flyer__cta">Join us as we invest to make disciples in “all nations” by 2022.<br>To learn more, email Martin Hale at mhale@harvestcompletion.org.</p>
  </article>
</body>
</html>
```